Design some Business Cards for Professional Cleaning company

Double sided card/ Standard card (I believe 3.5" x 2")
Unique
I have a logo already (Which is awesome)
Contact info: Marta Quill
martaquill@thebrightcornercleaning.example
(404) 555-0182
thebrightcornercleaning.example
Servicing Atlanta and Surrounding Areas
List of my services somehow without it looking cluttered
-Commercial/ New Construction clean up
-Residential/ rental property turn over
-move ins/move outs (Tenant)
-Pre/Post Event Clean Up
-Office Cleaning
-Restaurants and more!
I am open and versatile and very appreciative

```html
<!DOCTYPE html>
<html lang="en">
<head>
<meta charset="utf-8">
<title>The Bright Corner – Business Cards</title>
<link rel="stylesheet" href="https://fonts.googleapis.com/css2?family=Open+Sans:wght@300;400;700&display=swap">
<style>
  :root {
    --blue: #1a8fe0;
    --charcoal: #2f3236;
    --charcoal-deep: #26292c;
    --paper: #ffffff;
    --ink-light: #e4e6e8;
    --backdrop: #d9d6d1;
  }
  * { box-sizing: border-box; margin: 0; padding: 0; }
  html, body {
    width: 1200px; height: 900px; overflow: hidden;
    background: var(--backdrop);
    font-family: "Open Sans", sans-serif;
  }
  .card {
    position: absolute; left: 250px; width: 700px; height: 400px;
    overflow: hidden; box-shadow: 0 6px 18px rgba(0,0,0,.25);
  }
  .brand {
    position: absolute; top: 34px; right: 40px;
    display: flex; align-items: center; gap: 10px;
    font-weight: 700; font-size: 24px; letter-spacing: .3px;
  }
  .brand-dot { width: 16px; height: 16px; border-radius: 50%; }

  /* Back */
  .card-back { top: 40px; background: linear-gradient(160deg, var(--charcoal), var(--charcoal-deep)); }
  .card-back .brand { color: var(--paper); }
  .card-back .brand-dot { background: var(--paper); }
  .service-area {
    position: absolute; left: 56px; top: 110px;
    color: var(--blue); font-size: 19px; font-weight: 400;
  }
  .services { position: absolute; left: 56px; top: 150px; list-style: none; }
  .services li {
    display: flex; align-items: center; gap: 18px;
    color: var(--ink-light); font-size: 19px; font-weight: 300;
    line-height: 36px;
  }
  .services li::before {
    content: ""; width: 9px; height: 9px; border-radius: 50%;
    background: var(--blue); flex: none;
  }

  /* Front */
  .card-front { top: 460px; background: var(--paper); }
  .stripe-top { position: absolute; left: 0; top: 0; width: 100%; height: 10px; background: var(--blue); }
  .card-front .brand { color: var(--blue); }
  .card-front .brand-dot { background: var(--blue); }
  .name-tag {
    position: absolute; left: 0; top: 138px; height: 38px; padding: 0 22px 0 40px;
    background: var(--blue); color: var(--paper);
    display: flex; align-items: center; font-size: 20px; font-weight: 400; letter-spacing: 1px;
  }
  .name-tag strong { font-weight: 700; margin-left: 7px; }
  .divider { position: absolute; left: 0; top: 196px; width: 100%; height: 14px; background: var(--blue); }
  .contact-panel {
    position: absolute; left: 0; top: 210px; width: 100%; height: 180px;
    background: linear-gradient(160deg, var(--charcoal), var(--charcoal-deep));
  }
  .contacts { position: absolute; left: 40px; top: 24px; list-style: none; }
  .contacts li {
    display: flex; align-items: center; gap: 14px;
    color: var(--ink-light); font-size: 18px; font-weight: 300; line-height: 42px;
  }
  .contacts svg { width: 18px; height: 18px; flex: none; }
  .stripe-bottom { position: absolute; left: 0; bottom: 0; width: 100%; height: 10px; background: var(--blue); }
</style>
</head>
<body>

<section class="card card-back" aria-label="Card back">
  <div class="brand"><span class="brand-dot"></span>The Bright Corner</div>
  <p class="service-area">Servicing Atlanta and Surrounding Areas</p>
  <ul class="services">
    <li>Commercial/ New Construction clean up</li>
    <li>Residential/ rental property turn over</li>
    <li>move ins/move outs (Tenant)</li>
    <li>Pre/Post Event Clean Up</li>
    <li>Office Cleaning</li>
    <li>Restaurants and more!</li>
  </ul>
</section>

<section class="card card-front" aria-label="Card front">
  <div class="stripe-top"></div>
  <div class="brand"><span class="brand-dot"></span>The Bright Corner</div>
  <div class="name-tag">MARTA <strong>QUILL</strong></div>
  <div class="divider"></div>
  <div class="contact-panel">
    <ul class="contacts">
      <li>
        <svg viewBox="0 0 24 24" aria-hidden="true"><path fill="#1a8fe0" d="M6.6 10.8a15 15 0 0 0 6.6 6.6l2.2-2.2a1 1 0 0 1 1-.25 11.4 11.4 0 0 0 3.6.57 1 1 0 0 1 1 1V20a1 1 0 0 1-1 1A17 17 0 0 1 3 4a1 1 0 0 1 1-1h3.5a1 1 0 0 1 1 1c0 1.25.2 2.45.57 3.57a1 1 0 0 1-.25 1z"/></svg>
        (404) 555-0182
      </li>
      <li>
        <svg viewBox="0 0 24 24" aria-hidden="true"><rect x="2" y="5" width="20" height="14" rx="1" fill="#1a8fe0"/><path d="M2.5 6l9.5 7 9.5-7" fill="none" stroke="#2f3236" stroke-width="1.6"/></svg>
        thebrightcornercleaning.example
      </li>
      <li>
        <svg viewBox="0 0 24 24" aria-hidden="true"><circle cx="12" cy="12" r="10" fill="none" stroke="#1a8fe0" stroke-width="2"/><ellipse cx="12" cy="12" rx="4" ry="10" fill="none" stroke="#1a8fe0" stroke-width="1.6"/><path d="M2 12h20" stroke="#1a8fe0" stroke-width="1.6"/></svg>
        martaquill@thebrightcornercleaning.example
      </li>
    </ul>
  </div>
  <div class="stripe-bottom"></div>
</section>

</body>
</html>
```